Contact Page for Design Number 58170946

I would like to request a "Contact Us" page for the site delivered in Design Number 58170946.

1) The page should be responsive on desktop, tablet and mobile phone.
2) The page should have the following fields:
- Name (text)
- Email address (text)
- Topic (list: Question, Complaint, Appreciation)
- Subject (text)
- Message (textarea)
- Send (button)
3) I would like to get the html and css code.
4) I need to know explicitly the changes done to the css of the final version of Design Number 58170946 required for the new "Contact Us" page.

```html
<!DOCTYPE html>
<html lang="en">
<head>
<meta charset="UTF-8">
<title>Contact Us</title>
<link rel="stylesheet" href="https://fonts.googleapis.com/css2?family=Poppins:wght@400;500;600;700&display=swap">
<style>
  :root {
    --navy-deep: #162a4d;
    --navy: #213557;
    --label: #0f2044;
    --field-text: #333a44;
    --field-border: #dcdcdc;
    --accent: #f04b4b;
    --accent-edge: #c93636;
    --white: #ffffff;
  }
  * { box-sizing: border-box; margin: 0; padding: 0; }
  html, body { width: 941px; height: 1200px; overflow: hidden; background: var(--white); }
  body { position: relative; font-family: "Poppins", sans-serif; }

  .hero { position: absolute; left: 0; top: 0; width: 941px; height: 370px; }
  .hero-band { position: absolute; inset: 0; }
  .hero-title {
    position: absolute; left: 0; right: 0; top: 138px;
    text-align: center; color: var(--white);
    font-weight: 700; font-size: 70px; line-height: 1; letter-spacing: 1px;
  }

  .contact-form { position: absolute; inset: 0; pointer-events: none; }
  .contact-form > * { pointer-events: auto; }
  .field-label {
    position: absolute; color: var(--label);
    font-weight: 600; font-size: 27px; line-height: 1;
  }
  .field {
    position: absolute; height: 68px; width: 401px;
    border: 1px solid var(--field-border); border-radius: 4px;
    background: var(--white);
    box-shadow: 0 6px 16px rgba(0,0,0,0.07);
    font-family: "Poppins", sans-serif; font-size: 26px; color: var(--field-text);
    padding: 0 28px; outline: none;
  }
  .field::placeholder { color: var(--field-text); opacity: 1; }
  .field-select { appearance: none; -webkit-appearance: none; }
  .select-arrow { position: absolute; left: 425px; top: 618px; width: 16px; height: 12px; pointer-events: none; }
  .field-message { height: 300px; width: 817px; padding: 20px 28px; resize: none; line-height: 1.3; }

  .send-button {
    position: absolute; left: 378px; top: 1073px; width: 184px; height: 75px;
    border: none; border-radius: 38px;
    background: var(--accent);
    box-shadow: 0 4px 0 var(--accent-edge);
    color: var(--white); font-family: "Poppins", sans-serif;
    font-weight: 700; font-size: 27px; letter-spacing: 1px; cursor: pointer;
  }
</style>
</head>
<body>
  <header class="hero">
    <svg class="hero-band" width="941" height="370" viewBox="0 0 941 370" role="img" aria-label="Abstract navy background with soft flowing blobs and circles">
      <defs>
        <linearGradient id="heroFill" x1="0" y1="0" x2="0" y2="1">
          <stop offset="0" stop-color="#182c50"/>
          <stop offset="1" stop-color="#223658"/>
        </linearGradient>
      </defs>
      <path d="M0 0 H941 V288 Q470 444 0 276 Z" fill="url(#heroFill)"/>
    </svg>
    <h1 class="hero-title">Contact Us</h1>
  </header>

  <form class="contact-form" action="#" method="post">
    <label class="field-label" for="name" style="left:61px; top:416px;">Name</label>
    <input class="field" id="name" name="name" type="text" placeholder="Enter Your Name" style="left:61px; top:455px;">

    <label class="field-label" for="email" style="left:476px; top:416px;">Email</label>
    <input class="field" id="email" name="email" type="email" placeholder="Enter Email Address" style="left:477px; top:455px;">

    <label class="field-label" for="topic" style="left:61px; top:552px;">Topic</label>
    <select class="field field-select" id="topic" name="topic" style="left:61px; top:591px;">
      <option>Question</option>
      <option>Complaint</option>
      <option>Appreciation</option>
    </select>
    <svg class="select-arrow" viewBox="0 0 16 12" aria-hidden="true">
      <path d="M2 3 L8 9 L14 3" fill="none" stroke="#0f2044" stroke-width="2.4" stroke-linecap="round" stroke-linejoin="round"/>
    </svg>

    <label class="field-label" for="subject" style="left:476px; top:552px;">Subject</label>
    <input class="field" id="subject" name="subject" type="text" placeholder="Enter Your Subject" style="left:477px; top:591px;">

    <label class="field-label" for="message" style="left:61px; top:690px;">Message</label>
    <textarea class="field field-message" id="message" name="message" placeholder="Type Your Messages..." style="left:61px; top:730px;"></textarea>

    <button class="send-button" type="submit">SEND</button>
  </form>
</body>
</html>
```